IT services company needs a business card designed

-2 sided business card.-Front is going to be the logo raised (3D floating effect) on a black background. Make the logos spider web shiny silver and keep the spider the same design. -Back needs to have the following information:Darrel Sotho, Managing Partner, Cell: 738-402-1954, Website: Plankhorn.com, Email: Darrel@Plankhorn.com
Target Market(s)
IT Services
Industry/Entity Type
It Company
Contact Information for Business Card
-2 sided business card.
-Front is going to be the logo raised (3D floating effect) on a black background. Make the logos spider web shiny silver and keep the spider the same design.
-Back needs to have the following information:
Darrel Sotho, Managing Partner, Cell: 738-402-1954, Website: Plankhorn.com, Email: Darrel@Plankhorn.com

```html
<!DOCTYPE html>
<html lang="en">
<head>
<meta charset="utf-8">
<title>Plankhorn Business Card</title>
<link rel="stylesheet" href="https://fonts.googleapis.com/css2?family=Exo+2:wght@300;400;500&display=swap">
<style>
  :root {
    --backdrop: #2b2c2e;
    --card-dark: #111519;
    --card-glow: #1d3a4a;
    --accent: #1e9be0;
    --text-light: #e6ecef;
    --text-muted: #b9c4ca;
    --logo-ink: #9fb0b8;
  }
  * { margin: 0; padding: 0; box-sizing: border-box; }
  html, body {
    width: 1200px; height: 750px; overflow: hidden;
    background: var(--backdrop);
    font-family: "Exo 2", sans-serif;
  }
  .stage {
    position: relative; width: 1200px; height: 750px;
    display: flex; align-items: center; justify-content: center; gap: 40px;
  }
  .card {
    position: relative; width: 540px; height: 309px; overflow: hidden;
    background: radial-gradient(ellipse 60% 70% at 58% 40%, var(--card-glow) 0%, var(--card-dark) 70%);
  }
  .tab {
    position: absolute; width: 44px; height: 26px; background: var(--accent);
  }
  .tab--right { right: -22px; top: 58px; border-radius: 13px; }
  .tab--left { left: -22px; bottom: 70px; border-radius: 13px; }
  .tab--top { top: -13px; right: 120px; border-radius: 13px; }

  .logo {
    position: absolute; display: flex; align-items: center; gap: 10px;
    color: var(--logo-ink); font-weight: 500; letter-spacing: 0.08em; text-transform: uppercase;
  }
  .logo__dot { border-radius: 50%; background: var(--logo-ink); }
  .card--back .logo { left: 292px; top: 108px; font-size: 20px; }
  .card--back .logo__dot { width: 14px; height: 14px; }
  .card--front .logo { left: 50%; top: 50%; transform: translate(-50%, -50%); font-size: 34px; gap: 14px; }
  .card--front .logo__dot { width: 24px; height: 24px; }

  .holder { position: absolute; left: 34px; top: 42px; }
  .holder__name { color: var(--accent); font-size: 24px; font-weight: 400; letter-spacing: 0.04em; text-transform: uppercase; }
  .holder__role { color: var(--text-light); font-size: 11px; font-weight: 300; margin-top: 2px; }

  .contact-bar {
    position: absolute; left: 0; top: 178px; width: 150px; height: 112px;
    background: var(--accent); border-radius: 0 24px 24px 0;
    display: flex; flex-direction: column; justify-content: space-around; align-items: flex-end; padding: 8px 22px 8px 0;
  }
  .contact-bar svg { width: 18px; height: 18px; fill: none; stroke: #fff; stroke-width: 1.6; }
  .contact-list { position: absolute; left: 176px; top: 186px; list-style: none; }
  .contact-list li {
    display: flex; height: 32px; align-items: center; color: var(--text-light); font-size: 13px; font-weight: 300;
    border-left: 1px solid var(--text-muted); padding-left: 14px;
  }
  .contact-list .label { width: 82px; color: var(--text-muted); }
</style>
</head>
<body>
<main class="stage">
  <section class="card card--back" aria-label="Card back">
    <span class="tab tab--right"></span>
    <div class="holder">
      <h1 class="holder__name">Darrel Sotho</h1>
      <p class="holder__role">Managing Partner</p>
    </div>
    <div class="logo"><span class="logo__dot"></span>Plankhorn</div>
    <div class="contact-bar">
      <svg viewBox="0 0 24 24" aria-label="Phone"><rect x="7" y="2.5" width="10" height="19" rx="2"/><line x1="11" y1="18" x2="13" y2="18"/></svg>
      <svg viewBox="0 0 24 24" aria-label="Website"><circle cx="12" cy="12" r="9"/><ellipse cx="12" cy="12" rx="4" ry="9"/><line x1="3" y1="12" x2="21" y2="12"/></svg>
      <svg viewBox="0 0 24 24" aria-label="Email"><rect x="3" y="6" width="18" height="12" rx="1"/><polyline points="3,6 12,13 21,6"/></svg>
    </div>
    <ul class="contact-list">
      <li><span class="label">Cell:</span>738-402-1954</li>
      <li><span class="label">Website :</span>plankhorn.com</li>
      <li><span class="label">Email:</span>darrel@plankhorn.com</li>
    </ul>
  </section>

  <section class="card card--front" aria-label="Card front">
    <span class="tab tab--top"></span>
    <span class="tab tab--left"></span>
    <div class="logo"><span class="logo__dot"></span>Plankhorn</div>
  </section>
</main>
</body>
</html>
```